Full re-design of visual identity

We have just re-designed our logo and would like to apply it on our folders, business cards, stationery, and etc... we are attaching new logo + the material we need to re-design... we will provide full corel draw files to help make job easier and also because lot of icons and artwork can be still used...

any doubts we are at your disposal. thanks in advance.

Business

```html
<!DOCTYPE html>
<html lang="en">
<head>
<meta charset="utf-8">
<title>Lumora stationery set</title>
<link href="https://fonts.googleapis.com/css2?family=Montserrat:wght@400;600;700&display=swap" rel="stylesheet">
<style>
:root{
  --bg:#c6dddb;
  --teal:#a3d3cd;
  --teal-line:#e4f3f1;
  --paper:#f7f8f8;
  --ink:#2f3435;
  --grey:#7d8587;
  --soft-grey:#d6d9da;
  --emboss:#e3e6e6;
}
*{margin:0;padding:0;box-sizing:border-box}
html,body{width:1200px;height:1096px;overflow:hidden}
body{background:var(--bg);font-family:'Montserrat',sans-serif;color:var(--ink);position:relative}
.item{position:absolute;box-shadow:0 2px 6px rgba(40,70,70,.15)}
.brand-name{font-weight:600;color:var(--ink);letter-spacing:.25em;white-space:nowrap}

/* folder */
.folder{left:197px;top:110px;width:342px;height:452px;background:var(--teal)}
.folder-ring{position:absolute;left:62px;top:96px;width:218px;height:218px;border:1px solid var(--teal-line);border-radius:50%}
.folder .brand-name{position:absolute;left:0;right:0;top:196px;text-align:center;font-size:18px}
.folder-badge{position:absolute;left:148px;top:290px;width:46px;height:46px;border-radius:50%;background:var(--paper)}
.folder-url{position:absolute;left:0;right:0;top:411px;text-align:center;font-size:7px}
.folder-title{position:absolute;left:0;right:0;top:424px;text-align:center;font-size:9px;font-weight:600;letter-spacing:1px}

/* letterhead */
.letter{left:595px;top:258px;width:318px;height:449px;background:var(--paper)}
.letter-info{position:absolute;right:22px;top:20px;border-collapse:collapse;font-size:4px}
.letter-info td{border:1px solid var(--soft-grey);padding:2px 4px}
.letter-date{position:absolute;left:49px;top:84px;font-size:5.5px;color:var(--grey)}
.letter-title{position:absolute;left:49px;top:94px;font-size:8px;font-weight:700;letter-spacing:.8px}
.letter-body{position:absolute;left:49px;top:114px;width:222px;font-size:4.6px;line-height:1.75;color:var(--grey)}
.letter-body p{margin-bottom:6px}
.letter-sign{position:absolute;left:49px;top:296px;font-size:5px;font-weight:600}
.letter-field{position:absolute;left:49px;top:310px;width:148px;height:20px;background:var(--soft-grey)}
.letter-foot{position:absolute;left:49px;right:22px;top:407px;display:flex;justify-content:space-between;align-items:flex-start;font-size:4px;color:var(--grey);line-height:1.6}
.letter-foot strong{display:block;font-size:5.5px;color:var(--ink)}
.letter-foot .brand-name{font-size:7px;margin-top:2px}

/* business cards */
.card{left:401px;width:138px;height:75px}
.card-front{top:632px;background:var(--teal)}
.card-front .brand-name{position:absolute;left:0;right:0;top:25px;text-align:center;font-size:12px}
.card-rule{position:absolute;left:64px;top:50px;width:10px;border-top:1px solid var(--ink)}
.card-url{position:absolute;left:0;right:0;top:58px;text-align:center;font-size:5px}
.card-back{top:760px;background:var(--paper)}
.card-num{position:absolute;left:13px;top:12px;font-size:7px;font-weight:700}
.card-back .brand-name{position:absolute;left:34px;top:12px;font-size:12px;color:var(--emboss)}
.card-lines{position:absolute;left:13px;top:38px;width:114px;border-top:1px solid var(--ink);border-bottom:1px solid var(--ink);padding:2px 0;font-size:3.6px;line-height:2.1;white-space:nowrap}

/* compliment card (under envelope) */
.note{left:723px;top:813px;width:244px;height:171px;background:var(--paper)}
.note .brand-name{position:absolute;left:112px;top:24px;font-size:10px}
.note-url{position:absolute;left:112px;top:66px;font-size:6px}
.note-title{position:absolute;left:40px;top:78px;font-size:8px;font-weight:700;letter-spacing:1px;white-space:nowrap}
.note-name{position:absolute;left:18px;top:137px;font-size:6px;font-weight:700}
.note-name small{display:block;font-weight:400;font-size:4px;color:var(--grey)}
.note-addr{position:absolute;right:16px;top:137px;font-size:4px;line-height:1.7;color:var(--grey);text-align:right}

/* envelope */
.envelope{left:596px;top:760px;width:244px;height:174px;background:#fafbfb}
.envelope svg{position:absolute;inset:0}
.envelope-band{position:absolute;left:77px;top:0;width:91px;height:174px;background:var(--teal)}
.envelope-band .brand-name{position:absolute;left:0;right:0;top:26px;text-align:center;font-size:10px}
.envelope-url{position:absolute;left:0;right:0;top:158px;text-align:center;font-size:6px;font-weight:600}
</style>
</head>
<body>

<section class="item folder">
  <div class="folder-ring"></div>
  <p class="brand-name">LUMORA</p>
  <div class="folder-badge"></div>
  <p class="folder-url">www.lumora.com.br</p>
  <p class="folder-title">LUMORA - TELECOMUNICATION INTERNET</p>
</section>

<section class="item letter">
  <table class="letter-info">
    <tr><td>City Name, Country Name</td><td>123 Lorem Ipsum</td></tr>
    <tr><td>Web site</td><td></td></tr>
    <tr><td>Telephone / Fax</td><td>00.000.123.4567</td></tr>
  </table>
  <p class="letter-date">16 . August . 2013 . NY</p>
  <h1 class="letter-title">LUMORA - TELECOMUNICATION INTERNET</h1>
  <div class="letter-body">
    <p>Thank you for your interest in our new fibre internet plans. This letter confirms the details of your installation and the support hours of our local team in your city.</p>
    <p>Our technicians will visit your address during the week agreed with you. Please keep the modem close to a power outlet and make sure someone is at home to sign the service order when the work is done.</p>
    <p>If you have any questions, reply to this letter or call our help line at any time.</p>
  </div>
  <p class="letter-sign">Sed ut perspiciatis unde omnis iste natus</p>
  <div class="letter-field"></div>
  <div class="letter-foot">
    <div><strong>John Doe</strong>graphic designer</div>
    <div>t. 00.000.123.4567<br>e. contact@company.com</div>
    <div>123 E. 80 th Street<br>City Name, Country Name</div>
    <p class="brand-name">LUMORA</p>
  </div>
</section>

<section class="item card card-front">
  <p class="brand-name">LUMORA</p>
  <div class="card-rule"></div>
  <p class="card-url">www.lumora.com.br</p>
</section>

<section class="item card card-back">
  <p class="card-num">12</p>
  <p class="brand-name">LUMORA</p>
  <div class="card-lines">
    JOHN DOE, GRAPHIC DESIGNER, CONTACT@MAIL.COM<br>
    T. +12 34 56 78 XX . 123 STREET NAME . NY . COUNTRY
  </div>
</section>

<section class="item note">
  <p class="brand-name">LUMORA</p>
  <p class="note-url">www.lumora.com.br</p>
  <p class="note-title">LUMORA - TELECOMUNICATION INTERNET</p>
  <p class="note-name">John Doe<small>graphic designer</small></p>
  <p class="note-addr">123 E. 80 th Street, / City Name, Country Name<br>t. 00.000.123.4567<br>e. contact@company.com</p>
</section>

<section class="item envelope">
  <svg width="244" height="174" viewBox="0 0 244 174">
    <polyline points="0,0 122,92 244,0" fill="none" stroke="#dfe3e3" stroke-width="1"/>
    <path d="M0,174 100,96 M244,174 144,96" fill="none" stroke="#e6e9e9" stroke-width="1"/>
  </svg>
  <div class="envelope-band">
    <p class="brand-name">LUMORA</p>
    <p class="envelope-url">www.lumora.com.br</p>
  </div>
</section>

</body>
</html>
```